Executive recruiting firm in need of business card design

Executive recruiting firm looking for a sleek, classy and modern business card design; card itself will be square shape, rounded edges and soft touch paper, our colors are dark blues in the navy color scale, silvers and grays. Reference our website for a better idea of our company's feel and goals at Staffvex.com - our company message is "Lasting Teams Start With the Right Hire" this should be on the card

Industry/Entity Type

Business

```html
<!DOCTYPE html>
<html lang="en">
<head>
<meta charset="utf-8">
<title>Staffvex Business Card</title>
<link rel="stylesheet" href="https://fonts.googleapis.com/css2?family=Source+Sans+3:ital,wght@0,400;0,600;1,600&display=swap">
<style>
  :root {
    --backdrop: #e9e7e4;
    --card-dark: #1c1818;
    --card-light: #ffffff;
    --ink-light: #ffffff;
    --navy: #15173f;
  }
  * { margin: 0; padding: 0; box-sizing: border-box; }
  html, body {
    width: 1200px;
    height: 900px;
    overflow: hidden;
    background: var(--backdrop);
    font-family: "Source Sans 3", "Myriad Pro", Arial, sans-serif;
  }
  .canvas {
    position: relative;
    width: 1200px;
    height: 900px;
  }
  .card {
    position: absolute;
    border-radius: 18px;
    box-shadow: 0 6px 18px rgba(0, 0, 0, 0.18);
  }
  .card-back {
    left: 78px;
    top: 34px;
    width: 587px;
    height: 364px;
    background: var(--card-dark);
    color: var(--ink-light);
    text-align: center;
  }
  .holder-name {
    position: absolute;
    top: 80px;
    width: 100%;
    font-size: 23px;
    font-weight: 600;
    line-height: 1;
  }
  .holder-title {
    position: absolute;
    top: 106px;
    width: 100%;
    font-size: 16.5px;
    font-weight: 400;
    line-height: 1;
  }
  .contact-list {
    position: absolute;
    top: 173px;
    width: 100%;
    list-style: none;
    font-size: 16.5px;
    line-height: 24.5px;
  }
  .address {
    position: absolute;
    top: 269px;
    width: 100%;
    font-size: 16.5px;
    line-height: 1;
  }
  .card-front {
    left: 390px;
    top: 506px;
    width: 564px;
    height: 349px;
    background: var(--card-light);
  }
  .brand {
    position: absolute;
    left: 0;
    top: 110px;
    width: 100%;
    height: 124px;
    display: flex;
    align-items: center;
    justify-content: center;
  }
  .brand-name {
    color: var(--navy);
    font-size: 50px;
    font-weight: 400;
    line-height: 1;
  }
  .tagline {
    position: absolute;
    top: 297px;
    width: 100%;
    text-align: center;
    color: var(--navy);
    font-size: 18.5px;
    font-weight: 600;
    font-style: italic;
    line-height: 1;
  }
</style>
</head>
<body>
  <main class="canvas">
    <section class="card card-back" aria-label="Business card back">
      <h1 class="holder-name">Daniel Hart</h1>
      <p class="holder-title">Managing Director</p>
      <ul class="contact-list">
        <li>(044)-555-0182</li>
        <li>info@staffvex.com</li>
        <li>www.Staffvex.com</li>
      </ul>
      <p class="address">12345, Address Goes Here Country Name, 123456</p>
    </section>

    <section class="card card-front" aria-label="Business card front">
      <div class="brand">
        <span class="brand-name">Staffvex</span>
      </div>
      <p class="tagline">Lasting Teams Start With the Right Hire</p>
    </section>
  </main>
</body>
</html>
```